Realtor needs 8 1/2 x 11 flyer designed both sides

I uploaded a new word doc to be used under each of the pictures on the front page.

Colors

Designer to choose colors to be used in the design.

```html
<!DOCTYPE html>
<html lang="en">
<head>
<meta charset="utf-8">
<title>Realtor Flyer – Front and Back</title>
<link rel="stylesheet" href="https://fonts.googleapis.com/css2?family=Roboto+Condensed:wght@300;400;700&family=Roboto:wght@300;400;700&display=swap">
<style>
  :root {
    --stage: #3d3d3d;
    --paper: #ffffff;
    --royal: #1d45a8;
    --royal-deep: #163a92;
    --royal-soft: #3b5fbf;
    --orange: #e07c15;
    --orange-deep: #c9690c;
    --peach: #f4dccb;
    --ink: #2b2b2b;
    --grey-text: #9a9a9a;
    --rule-grey: #cfcfcf;
    --brand-blue: #1c4fd1;
    --band-rule: #f0b57a;
  }
  * { box-sizing: border-box; margin: 0; padding: 0; }
  html, body { width: 1200px; height: 863px; overflow: hidden; }
  body { background: var(--stage); position: relative; font-family: "Roboto Condensed", sans-serif; }

  .sheet { position: absolute; top: 82px; width: 522px; height: 673px; background: var(--paper); overflow: hidden; }
  .sheet--front { left: 60px; background: linear-gradient(#fafafa, #f3f3f3); }
  .sheet--back { left: 624px; }

  .sheet-label { position: absolute; top: 786px; color: #f0f0f0; font-family: "Roboto", sans-serif; font-size: 20px; letter-spacing: 5px; font-weight: 400; transform: translateX(-50%); }
  .sheet-label--front { left: 324px; }
  .sheet-label--back { left: 882px; }

  /* Front: outgoing agent panel */
  .outgoing-panel { position: absolute; left: 0; top: 0; width: 272px; height: 673px; background: linear-gradient(160deg, var(--royal-soft) 0%, var(--royal) 45%, var(--royal-deep) 100%); border-bottom-right-radius: 30px; box-shadow: 3px 0 6px rgba(0,0,0,.25); }
  .title-tab { position: absolute; left: 0; top: 0; width: 272px; height: 93px; background: linear-gradient(180deg, #ee8a1e, var(--orange-deep)); border-top-right-radius: 36px; border-bottom-right-radius: 36px; padding: 18px 0 0 23px; color: #fff; box-shadow: 0 3px 5px rgba(0,0,0,.3); }
  .title-tab__main { font-weight: 700; font-size: 38px; line-height: 34px; letter-spacing: -.3px; }
  .title-tab__sub { font-weight: 400; font-size: 28px; line-height: 30px; }

  .ghost-name { position: absolute; color: rgba(255,255,255,.18); font-weight: 400; text-transform: uppercase; line-height: 1; }
  .ghost-name--vertical { left: 19px; top: 302px; font-size: 58px; transform: rotate(-90deg); transform-origin: 0 0; }
  .ghost-name--wide { left: 291px; top: 12px; font-size: 92px; color: var(--peach); letter-spacing: 2px; font-weight: 300; }

  .portrait { position: absolute; border-radius: 50%; }
  .portrait--outgoing { left: 79px; top: 158px; width: 152px; height: 152px; background: radial-gradient(circle at 50% 40%, #d9b6a0 0 22%, #2a2a2a 23% 60%, #c8c8c8 61%); border: 6px solid #eeeeee; box-shadow: 0 2px 6px rgba(0,0,0,.4); }
  .portrait--incoming { left: 324px; top: 158px; width: 150px; height: 150px; background: radial-gradient(circle at 50% 38%, #e3c19e 0 24%, #d4b07a 25% 40%, #1f1f1f 41% 75%, #ffffff 76%); border: 6px solid var(--orange); box-shadow: 0 2px 6px rgba(0,0,0,.3); }

  .letter { position: absolute; top: 325px; font-size: 9.3px; line-height: 11.2px; text-align: justify; }
  .letter p + p { margin-top: 12px; }
  .letter--outgoing { left: 23px; width: 227px; color: #fff; }
  .letter--incoming { left: 291px; width: 208px; color: var(--ink); }

  .agent-card { position: absolute; top: 578px; }
  .agent-card--outgoing { left: 22px; color: #fff; }
  .agent-card--incoming { left: 290px; color: var(--ink); }
  .agent-card__name { font-weight: 700; font-size: 20px; line-height: 22px; text-transform: uppercase; }
  .agent-card__name .first { color: var(--orange); }
  .agent-card--outgoing .agent-card__name .last { color: var(--orange); }
  .agent-card--outgoing .agent-card__name .first { color: #fff; }
  .agent-card__phone { font-weight: 700; font-size: 14px; margin-top: 8px; line-height: 16px; }
  .agent-card__meta { font-size: 8.6px; line-height: 11.2px; margin-top: 3px; }

  .column-rule { position: absolute; left: 276px; top: 145px; width: 2px; height: 440px; background: linear-gradient(rgba(0,0,0,0), rgba(0,0,0,.12), rgba(0,0,0,0)); }

  /* Back: mailing side */
  .address-window { position: absolute; left: 37px; top: 28px; width: 310px; height: 137px; border: 1.5px solid var(--rule-grey); border-radius: 12px; }
  .address-window__text { position: absolute; left: 97px; top: 52px; font-family: "Roboto", sans-serif; font-weight: 300; color: var(--grey-text); font-size: 15px; line-height: 18px; }
  .postage-indicia { position: absolute; left: 414px; top: 32px; width: 77px; height: 76px; border: 1px solid #222; font-family: "Roboto", sans-serif; font-size: 10px; line-height: 12px; text-align: center; padding-top: 8px; color: #111; }
  .postage-indicia b { font-weight: 700; }

  .beach-scene { position: absolute; left: 0; top: 250px; width: 522px; height: 298px; background: linear-gradient(180deg, #ffffff 0%, #eeeeee 30%, #e2e2e2 55%, #d3d3d3 70%, #e6e6e6 85%, #f2f2f2 100%); }

  .brand-name { position: absolute; left: 130px; width: 270px; top: 262px; text-align: center; font-family: "Roboto Condensed", sans-serif; font-weight: 400; color: var(--brand-blue); z-index: 2; }
  .brand-name__first { display: block; font-size: 36px; line-height: 36px; letter-spacing: 2px; text-transform: uppercase; }
  .brand-name__last { display: block; font-size: 44px; line-height: 46px; letter-spacing: 1px; }
  .brand-title { position: absolute; left: 130px; width: 270px; top: 348px; text-align: center; font-family: "Roboto Condensed", sans-serif; font-size: 10px; letter-spacing: 1px; color: var(--ink); z-index: 2; }

  .portrait--back { position: absolute; left: 0; top: 362px; width: 218px; height: 311px; border-radius: 0; background: linear-gradient(180deg, #d8b98a 0%, #e2c3a4 40%, #2a2a2a 75%, #1c1c1c 100%); z-index: 1; }

  .contact-band { position: absolute; left: 175px; top: 548px; width: 347px; height: 125px; background: var(--paper); border-top: 4px solid var(--band-rule); z-index: 1; }
  .contact-band .agent-card { top: 22px; left: 50px; }
  .contact-band .agent-card__name { font-size: 22px; line-height: 24px; }
  .contact-band .agent-card__phone { font-size: 15px; margin-top: 6px; }
  .contact-band .agent-card__meta { font-size: 9.5px; line-height: 12.5px; }
  .partner-mark { position: absolute; left: 252px; top: 30px; width: 80px; text-align: center; font-family: "Roboto Condensed", sans-serif; font-weight: 700; font-size: 13px; line-height: 15px; color: var(--royal); }
  .partner-mark__dot { display: block; width: 34px; height: 34px; margin: 0 auto 5px; border-radius: 50%; background: var(--royal); }
</style>
</head>
<body>

<section class="sheet sheet--front" aria-label="Flyer front">
  <div class="outgoing-panel">
    <span class="ghost-name ghost-name--vertical" aria-hidden="true">Marla</span>
  </div>
  <header class="title-tab">
    <div class="title-tab__main">YOUR TITLE</div>
    <div class="title-tab__sub">GOES HERE</div>
  </header>
  <span class="ghost-name ghost-name--wide" aria-hidden="true">LENA</span>
  <div class="column-rule"></div>

  <div class="portrait portrait--outgoing" role="img" aria-label="Portrait photo of retiring realtor Marla Bennett"></div>
  <div class="portrait portrait--incoming" role="img" aria-label="Portrait photo of realtor Lena Whitford"></div>

  <article class="letter letter--outgoing">
    <p>I have exciting and bittersweet news I want to share with my Harbor Ridge clients, friends and neighbors. After 40 (some-thing) years in the Real Estate business, I have decided to retire. Some of you may last month I sold my Harbor Ridge home and moved to the beautiful Oak Meadow community in Canyon Vista. My husband and I wanted to scale down and have time to enjoy retirement, together. I have been so blessed to have had an illustrious career in Real Estate and I want to thank you with a most grateful heart for giving me the opportu-nity to work with you. I have enjoyed every minute.</p>
    <p>I'm happy and proud to be turning my business over to Lena Whitford, fellow Summit Realty agent. She and I have enjoyed a very close working relationship for many years and there is nobody else except Lena I'd consider turning my business over to. Lena is .... I will add verbiage here conveying your thoughts about me. Please contact me if you'd like a personal introduc-tion to Lena or contact her directly. Remember to mention me when you contact Lena and let her know that we know each other. I wish you the very best and please say hello when you see me in the neighborhood.</p>
  </article>

  <article class="letter letter--incoming">
    <p>I know many of you, but for those whom I do not, I'd like to introduce myself. I've been a resident of Harbor Ridge for almost 23 years now. I've loved our neighborhood from the first time I discovered it. From our beautiful parks to our fabulous pool and amenities, it's hard to beat our won-derful community.</p>
    <p>I always say where we live is the next best thing to living on a tropical island. I've traveled to many and I'm always happy to come back to my Harbor Ridge home My passion for this area is why I'm in Real Estate. I consider myself incredibly fortunate to sell homes and help people pur-chase homes in an area that I love with all my heart.</p>
    <p>Marla and I have been close colleagues for the last 8 years, both working as Realtors and long time residents of Harbor Ridge. I am most grateful for our working relation-ship and the friendship we have formed. I am humbled by her trust and respect for me. Please feel welcome to call on me for all things home-related. I will look forward to meeting you!</p>
  </article>

  <div class="agent-card agent-card--outgoing">
    <div class="agent-card__name"><span class="first">Marla</span> <span class="last">Bennett</span></div>
    <div class="agent-card__phone">555.201.4836</div>
    <div class="agent-card__meta">Realtor®<br>Marla@MarlaBennett.example<br>DRE# 00123456</div>
  </div>

  <div class="agent-card agent-card--incoming">
    <div class="agent-card__name"><span class="first">Lena</span> <span class="last">Whitford</span></div>
    <div class="agent-card__phone">555.318.7420</div>
    <div class="agent-card__meta">Realtor®<br>Lena@LenaWHomes.example<br>DRE# 01987654</div>
  </div>
</section>

<section class="sheet sheet--back" aria-label="Flyer back">
  <div class="address-window">
    <div class="address-window__text">Local<br>Postal Customer</div>
  </div>
  <div class="postage-indicia">PRSRT STD<br>ECRWSS<br>U.S. POSTAGE<br><b>PAID</b><br>EDDM RETAIL</div>

  <div class="beach-scene" role="img" aria-label="Soft grey beach scene with palm trees and ocean"></div>
  <div class="brand-name"><span class="brand-name__first">Lena</span><span class="brand-name__last">Whitford</span></div>
  <div class="brand-title">REALTOR®</div>
  <div class="portrait portrait--back" role="img" aria-label="Photo of realtor Lena Whitford"></div>

  <div class="contact-band">
    <div class="agent-card agent-card--incoming">
      <div class="agent-card__name"><span class="first">Lena</span> <span class="last">Whitford</span></div>
      <div class="agent-card__phone">555.318.7420</div>
      <div class="agent-card__meta">Realtor®<br>Lena@LenaWHomes.example<br>DRE# 01987654</div>
    </div>
    <div class="partner-mark"><span class="partner-mark__dot"></span>SUMMIT REALTY</div>
  </div>
</section>

<div class="sheet-label sheet-label--front">FRONT</div>
<div class="sheet-label sheet-label--back">BACK</div>

</body>
</html>
```